Unique and Affordable skin care business needs new business card

I currently have business cards that were designed on this site, but I am looking for a little update to my cards. I have recently relocated to a new location and need to update that information, as well as I would like to specify that not only do I do all skin care services at a very affordable price, but I also now do eyelash extensions, which are very much in demand!! I would like to include the pictures of my current business cards for ideas on how to change them and refresh them. My business name is Glow Haven by Maren my tag line is unique and affordable skin care just for YOU.

Industry/Entity Type

Business

```html
<!DOCTYPE html>
<html lang="en">
<head>
<meta charset="utf-8">
<title>Glow Haven by Maren – Business Card</title>
<link href="https://fonts.googleapis.com/css2?family=Jost:wght@400;500&family=Great+Vibes&family=Cormorant+Garamond:ital,wght@1,600&display=swap" rel="stylesheet">
<style>
  :root {
    --page-bg: #ece8e2;
    --card-white: #f6f7f8;
    --ink: #1d1d22;
    --front-deep: #2a1236;
    --front-red: #d8191f;
    --front-orange: #f28a1a;
    --front-blue: #2b6fd6;
    --front-violet: #8b2a8f;
    --wordmark: #ffffff;
    --name-pink: #e0409e;
    --name-blue: #3a67c9;
    --wash-blue: #7fb8e6;
    --wash-pink: #e7a6cf;
    --shadow: rgba(40, 30, 20, 0.25);
  }
  * { margin: 0; padding: 0; box-sizing: border-box; }
  html, body { width: 1200px; height: 1000px; overflow: hidden; }
  body { background: var(--page-bg); position: relative; }

  .card {
    position: absolute;
    border-radius: 18px;
    overflow: hidden;
    box-shadow: 0 12px 30px var(--shadow);
  }

  /* Front */
  .card-front { left: 70px; top: 130px; width: 580px; height: 330px; }
  .front-art {
    position: absolute; inset: 0;
    background:
      radial-gradient(circle at 22% 60%, var(--front-blue) 0%, transparent 38%),
      radial-gradient(circle at 40% 78%, var(--front-orange) 0%, transparent 30%),
      radial-gradient(circle at 62% 40%, var(--front-red) 0%, transparent 45%),
      radial-gradient(circle at 88% 70%, var(--front-violet) 0%, transparent 40%),
      linear-gradient(135deg, #1c2f6e 0%, var(--front-violet) 35%, var(--front-red) 60%, var(--front-deep) 100%);
  }
  .front-text { position: absolute; left: 60px; top: 112px; font-family: "Jost", sans-serif; }
  .tagline {
    font-size: 11px; letter-spacing: 1.6px; text-transform: uppercase;
    color: var(--wordmark); margin-left: 4px;
  }
  .wordmark {
    font-size: 54px; font-weight: 500; letter-spacing: 3px;
    color: var(--wordmark); line-height: 1; text-transform: uppercase; margin-top: 4px;
  }
  .wordmark-sub {
    display: block; font-size: 26px; letter-spacing: 1px; text-transform: none;
    text-align: right; margin-top: 6px; margin-right: 10px;
  }

  /* Back */
  .card-back { left: 540px; top: 500px; width: 600px; height: 340px; background: var(--card-white); }
  .back-art {
    position: absolute; right: 0; top: 0; width: 230px; height: 100%;
    background:
      radial-gradient(ellipse at 55% 35%, var(--wash-blue) 0%, transparent 55%),
      radial-gradient(ellipse at 30% 70%, var(--wash-pink) 0%, transparent 50%),
      linear-gradient(90deg, var(--card-white) 0%, #dfeaf6 40%, #f3dcec 100%);
  }
  .specialties {
    position: absolute; left: 30px; top: 20px; right: 20px;
    font-family: "Cormorant Garamond", serif; font-style: italic; font-weight: 600;
    font-size: 14px; color: var(--ink); letter-spacing: 0.3px;
  }
  .holder-name {
    position: absolute; left: 30px; top: 66px;
    font-family: "Great Vibes", cursive; font-size: 70px; line-height: 1;
  }
  .holder-name .first { color: var(--name-pink); }
  .holder-name .last { color: var(--name-blue); }
  .holder-title {
    position: absolute; left: 180px; top: 146px;
    font-family: "Cormorant Garamond", serif; font-style: italic; font-weight: 600;
    font-size: 15px; color: var(--ink);
  }
  .contact, .locations {
    position: absolute;
    font-family: "Cormorant Garamond", serif; font-style: italic; font-weight: 600;
    font-size: 15px; color: var(--ink); list-style: none;
  }
  .contact { left: 30px; top: 228px; }
  .locations { left: 250px; top: 248px; }
  .contact li, .locations li { display: flex; align-items: center; gap: 8px; height: 28px; }
  .locations li { justify-content: space-between; width: 330px; }
  .icon { width: 14px; height: 14px; flex: none; }
</style>
</head>
<body>

<section class="card card-front" aria-label="Card front">
  <div class="front-art" role="img" aria-label="Abstract glowing hexagon light pattern in blue, red, orange and violet"></div>
  <div class="front-text">
    <p class="tagline">Unique and affordable skin care just for you</p>
    <h1 class="wordmark">Glow Haven<span class="wordmark-sub">by maren</span></h1>
  </div>
</section>

<section class="card card-back" aria-label="Card back">
  <div class="back-art" role="img" aria-label="Watercolor portrait illustration in soft blue and pink"></div>
  <p class="specialties">LUXELASH Certified Extensionist &bull; Specializing in Veridia Skin Care Products</p>
  <h2 class="holder-name"><span class="first">Maren</span> <span class="last">Holt</span></h2>
  <p class="holder-title">Licensed Esthetician</p>

  <ul class="contact">
    <li>
      <svg class="icon" viewBox="0 0 14 14"><rect x="3" y="1" width="8" height="12" rx="1.5" fill="none" stroke="#1d1d22" stroke-width="1.4"/><line x1="6" y1="11" x2="8" y2="11" stroke="#1d1d22" stroke-width="1.2"/></svg>
      970-555-0142
    </li>
    <li>
      <svg class="icon" viewBox="0 0 14 14"><circle cx="7" cy="7" r="5.8" fill="none" stroke="#1d1d22" stroke-width="1.4"/><ellipse cx="7" cy="7" rx="2.4" ry="5.8" fill="none" stroke="#1d1d22" stroke-width="1"/><line x1="1.2" y1="7" x2="12.8" y2="7" stroke="#1d1d22" stroke-width="1"/></svg>
      glowhavenbymaren.com
    </li>
  </ul>

  <ul class="locations">
    <li>218 Birch Ave. Lakeview, Co.
      <svg class="icon" viewBox="0 0 14 14"><path d="M7 13 C3 8.5 2.5 6.5 2.5 5 a4.5 4.5 0 0 1 9 0 c0 1.5 -0.5 3.5 -4.5 8z" fill="none" stroke="#1d1d22" stroke-width="1.3"/><circle cx="7" cy="5" r="1.6" fill="#1d1d22"/></svg>
    </li>
    <li>5120 Elm Ridge Rd., Ste #4 Fairmont, Co.
      <svg class="icon" viewBox="0 0 14 14"><path d="M7 13 C3 8.5 2.5 6.5 2.5 5 a4.5 4.5 0 0 1 9 0 c0 1.5 -0.5 3.5 -4.5 8z" fill="none" stroke="#1d1d22" stroke-width="1.3"/><circle cx="7" cy="5" r="1.6" fill="#1d1d22"/></svg>
    </li>
  </ul>
</section>

</body>
</html>
```